" O escritório Brunoro Arquitetura desenvolve projetosarquitetônicos e interiores, além de acompanhamento e administraçãao de obras. Tem a frente de sua gestão a arquiteta Mariana Forteso, que prioriza o atendimento exclusivo e diferenciado a cada um dos clientes, estabelecendo assim uma relação de proximidade, confiança e fidelização. Todos os projetos são desenvolvidos de acordo com o perfil do cliente, buscando sempre soluções inovadoras, criativas e acessíveis, em muitos casos utilizando materiais e soluções alternativas ao convencional, marca do escritório. O espaço físico do escritório reflete essa proposta de inovação e criatividade, que permite a acessibilidade da arquitetura a qualquer pessoa, desmistificando o status de que a boa arquitetura é acessível somente àqueles que possuem um alto poder aquisitivo. Todo o processo de concepção e posterior execução dos trabalhos é realizada entre os profissionais envolvidos e os clientes com total transparência, sendo a política de trabalho do escritório focada na ética, honestidade e respeito ao cliente, não havendo portanto o recebimento de reservas técnicas ou comissões de lojistas e empresas terceiras, para indicação de produtos. Assim, trabalhamos com total liberdade na concepção e especificação de materiais e soluções nos projetos. O escritório também tem ligação forte com as escolas de arquitetura da cidade, sendo um local de estágio e constante aprendizado para estudantes, que adquirem experiência profissional junto aos membros do escritório. A linguagem dos projetos, que deve se refletir na identidade visual da marca, busca a simplicidade dos materiais e formas, aplicadas da forma correta, gerando resultados simples, porém sofisticados. Priorizamos o uso dos materiais naturais em todos os projetos, mas prioritariamente o uso da madeira natural. Trabalhamos sempre com muito respeito pela história dos lugares, procurando sempre que possível preservar características originais que dão identidade aos lugares. "

```html
<!DOCTYPE html>
<html lang="pt-BR">
<head>
<meta charset="utf-8">
<title>Assinatura de email — Brunoro Arquitetura</title>
<link href="https://fonts.googleapis.com/css2?family=Open+Sans:wght@300;400&family=Roboto+Condensed:wght@700&display=swap" rel="stylesheet">
<style>
  :root {
    --bg-center: #f6f6f6;
    --bg-edge: #b4b5b6;
    --tab: #5f6163;
    --panel: #6d6f71;
    --stripe: #c9cacc;
    --text-light: #e3e4e5;
    --text-white: #ffffff;
    --text-muted: #b3b5b7;
  }
  html, body {
    margin: 0;
    width: 1200px;
    height: 1200px;
    overflow: hidden;
  }
  .canvas {
    position: relative;
    width: 1200px;
    height: 1200px;
    background: radial-gradient(ellipse at 50% 45%, var(--bg-center) 0%, #dcdcdd 45%, var(--bg-edge) 100%);
    font-family: "Open Sans", Arial, sans-serif;
  }
  .section-tab {
    position: absolute;
    left: 72px;
    top: 24px;
  }
  .section-tab__label {
    position: absolute;
    left: 82px;
    top: 34px;
    margin: 0;
    font-family: "Roboto Condensed", "Arial Narrow", sans-serif;
    font-weight: 700;
    font-size: 24px;
    color: var(--text-white);
    letter-spacing: 0.2px;
    line-height: 43px;
  }
  .signature {
    position: absolute;
    left: 89px;
    top: 446px;
    width: 1022px;
    height: 308px;
  }
  .signature__stripe {
    height: 17px;
    background: var(--stripe);
  }
  .signature__panel {
    position: relative;
    height: 291px;
    background: var(--panel);
  }
  .brand {
    position: absolute;
    left: 40px;
    top: 50px;
    width: 260px;
    text-align: center;
  }
  .brand__mark {
    display: block;
    width: 58px;
    height: 58px;
    margin: 0 auto;
    border: 3px solid var(--text-white);
    box-sizing: border-box;
  }
  .brand__name {
    margin: 50px 0 0;
    font-size: 24px;
    font-weight: 400;
    line-height: 30px;
    color: var(--text-white);
    white-space: nowrap;
  }
  .brand__web {
    position: absolute;
    left: 60px;
    top: 226px;
    margin: 0;
    font-size: 22px;
    font-weight: 400;
    line-height: 30px;
    color: var(--text-white);
  }
  .contact {
    position: absolute;
    right: 55px;
    top: 30px;
    text-align: right;
    color: var(--text-light);
    font-weight: 400;
  }
  .contact p { margin: 0; }
  .contact__name {
    font-size: 27px;
    font-weight: 300;
    color: var(--text-muted);
    line-height: 36px;
  }
  .contact__reg {
    font-size: 22px;
    line-height: 30px;
  }
  .contact__address {
    margin-top: 10px !important;
    font-size: 22px;
    line-height: 27px;
  }
  .contact__phones {
    margin-top: 18px !important;
    font-size: 22px;
    line-height: 30px;
  }
  .contact__phones-label { color: var(--text-muted); font-weight: 300; }
  .contact__mail {
    font-size: 22px;
    line-height: 34px;
  }
</style>
</head>
<body>
<main class="canvas">
  <div class="section-tab">
    <svg width="380" height="60" viewBox="0 0 380 60" aria-hidden="true">
      <polygon points="0,10 356,10 346,53 0,53" fill="var(--tab)"/>
      <polygon points="343,0 375,0 368,24" fill="var(--tab)"/>
    </svg>
  </div>
  <p class="section-tab__label">ASSINATURA DE EMAIL</p>

  <section class="signature" aria-label="Assinatura de email">
    <div class="signature__stripe"></div>
    <div class="signature__panel">
      <div class="brand">
        <span class="brand__mark" aria-hidden="true"></span>
        <p class="brand__name">Brunoro Arquitetura</p>
      </div>
      <p class="brand__web">www.brunoroarq.com.br</p>

      <div class="contact">
        <p class="contact__name">Mariana Forteso</p>
        <p class="contact__reg">CAU - 54321-07</p>
        <p class="contact__address">Rua das Palmeiras, 845<br>Bairro: Centro | CEP: 04512-330<br>São Paulo/SP</p>
        <p class="contact__phones"><span class="contact__phones-label">Telefones:</span> (11) 4020-7731 | (11) 98450-2216</p>
        <p class="contact__mail">contato@brunoroarq.com.br</p>
      </div>
    </div>
  </section>
</main>
</body>
</html>
```